Orlenby Advisory business card

Premium business card required
I have attached the brand as a powerpoint template but this can be made to look very up market, I have also attached my BIO for title reasons and to give you a feel for my skills
front of card
Derek Holloway
Managing Director Orlenby Advisory
Retail, Customer-Led Experience, Transformation and Maximising Shareholder Return
Mobile +61(0)418557392
Email derekorlenbyadvisory.com
back of card

ORLENBY ADVISORY’ OFFERING

We transform customer environments to extract benefits while elevating service levels;
We release millions of dollars in self-funding through continuous improvement;
We see CX as a key differentiator, proactively guarding share from market disrupters;
We re-invent service and create front-end of the future.

```html
<!DOCTYPE html>
<html lang="en">
<head>
<meta charset="utf-8">
<title>Orlenby Advisory business card</title>
<link href="https://fonts.googleapis.com/css2?family=Open+Sans:wght@400;600;700&display=swap" rel="stylesheet">
<style>
  :root {
    --page: #e9e9e9;
    --gold-dark: #c6ab34;
    --gold-light: #eadf62;
    --gold-text: #c9a92c;
    --white: #ffffff;
    --ink: #4a4a4a;
    --ink-soft: #5c5c5c;
    --band: #575757;
    --divider: #d4d4d4;
  }
  * { margin: 0; padding: 0; box-sizing: border-box; }
  html, body { width: 1200px; height: 900px; overflow: hidden; }
  body {
    background: var(--page);
    font-family: "Open Sans", Arial, sans-serif;
    position: relative;
  }
  .card {
    position: absolute;
    left: 260px;
    width: 680px;
    height: 388px;
    box-shadow: 0 6px 18px rgba(0,0,0,.18);
    overflow: hidden;
  }

  /* Back of card */
  .card-back {
    top: 45px;
    background: linear-gradient(200deg, var(--gold-dark) 0%, #d7c445 55%, var(--gold-light) 100%);
    color: var(--white);
    text-align: center;
    padding-top: 70px;
  }
  .brand {
    display: inline-flex;
    align-items: center;
    gap: 14px;
    font-weight: 700;
    font-size: 44px;
    letter-spacing: .5px;
    line-height: 1;
    white-space: nowrap;
  }
  .brand-dot {
    width: 46px; height: 46px; border-radius: 50%;
    background: currentColor;
    flex: none;
  }
  .offering-title {
    margin-top: 46px;
    font-weight: 700;
    font-size: 17px;
  }
  .offering-list {
    list-style: none;
    margin-top: 12px;
    font-size: 13.5px;
    line-height: 1.45;
  }

  /* Front of card */
  .card-front {
    top: 467px;
    background: var(--white);
  }
  .front-logo {
    position: absolute;
    left: 36px; top: 140px;
  }
  .front-logo .brand { font-size: 30px; gap: 10px; color: var(--ink); }
  .front-logo .brand-dot { width: 34px; height: 34px; background: var(--gold-text); }
  .divider {
    position: absolute;
    left: 382px; top: 60px;
    width: 1px; height: 190px;
    background: linear-gradient(to bottom, transparent, var(--divider) 25%, var(--divider) 75%, transparent);
  }
  .contact {
    position: absolute;
    left: 400px; top: 72px;
    color: var(--ink-soft);
  }
  .person-name {
    color: var(--gold-text);
    font-weight: 700;
    font-size: 17px;
    letter-spacing: .3px;
  }
  .person-title {
    margin-top: 6px;
    font-size: 11.5px;
    line-height: 1.5;
    white-space: nowrap;
  }
  .contact-lines { list-style: none; margin-top: 16px; font-size: 13.5px; line-height: 1.6; }
  .contact-lines li { display: flex; align-items: center; gap: 9px; }
  .contact-lines svg { width: 12px; height: 12px; fill: var(--gold-text); flex: none; }
  .band-line {
    position: absolute; left: 0; right: 0; bottom: 64px;
    height: 3px; background: var(--gold-text);
  }
  .web-band {
    position: absolute; left: 0; right: 0; bottom: 0;
    height: 56px;
    background: var(--band);
    color: var(--white);
    font-weight: 600;
    font-size: 17px;
    letter-spacing: 3px;
    display: flex; align-items: center; justify-content: center;
    padding-left: 120px;
  }
</style>
</head>
<body>

<section class="card card-back">
  <div class="brand"><span>Orlenby Advisory</span><span class="brand-dot"></span></div>
  <h2 class="offering-title">Orlenby Advisory Offering</h2>
  <ul class="offering-list">
    <li>We transform customer environments to extract benefits while elevating service levels;</li>
    <li>We release millions of dollars in self-funding through continuous improvement;</li>
    <li>We see CX as a key differentiator, proactively guarding share from market disrupters;</li>
    <li>We re-invent service and create front-end of the future.</li>
  </ul>
</section>

<section class="card card-front">
  <div class="front-logo">
    <div class="brand"><span>Orlenby Advisory</span><span class="brand-dot"></span></div>
  </div>
  <div class="divider"></div>
  <div class="contact">
    <h1 class="person-name">DEREK HOLLOWAY</h1>
    <p class="person-title">Managing Director Orlenby Advisory<br>Retail, Customer-Led Experience<br>Transformation &amp; Maximising Shareholder Return</p>
    <ul class="contact-lines">
      <li><svg viewBox="0 0 12 12"><rect x="2.5" y="0" width="7" height="12" rx="1.2"/><rect x="3.7" y="1.5" width="4.6" height="7.5" fill="#fff"/></svg>+61(0)418557392</li>
      <li><svg viewBox="0 0 12 12"><rect x="0" y="2" width="12" height="8" rx="1"/><path d="M0.6 2.6 6 6.6 11.4 2.6" stroke="#fff" stroke-width="1.1" fill="none"/></svg>dh@derekorlenbyadvisory.com</li>
    </ul>
  </div>
  <div class="band-line"></div>
  <div class="web-band">www.derekorlenbyadvisory.com</div>
</section>

</body>
</html>
```